Bright Dune Series- Face & Body Oil Label

Hi,
I need a label design for a new brand- "Bright Dune Series". Modern and expensive looking. Any color scheme. Feel free to be creative! (I'm not set on the brand name above... I was also thinking maybe "LUXA" or "PuraGlow".
-Packaging: 4oz / 118mL clear glass "boston round" bottle with a white treatment pump. The product is an oil so it has a golden tint.
-Product: 4oz Biotin & Marula Face & Body Oil (note that the featured ingredients will change. Others will be "Rosehip & Vitamin E", "Lavender & Hemp Seed Oil", "Coconut Oil & Vitamin C"
-Label size: 5" x 2.5" rounded corners
-Main Highlight: "Moisturizing & Healing"
-Other Highlights:
-----non-greasy
-----all-natural
-----paraben-free
-----vegan
(feel free to use icon symbols)
-Ingredient deck attached
-Other info:
----made in Los Angeles, CA
----manufactured by Willowmark Blends LLC
----UPC
The main thing here is the logo and textures to the label. I can fill in / rearrange the info after.
Thank you,
Theo

```html
<!DOCTYPE html>
<html lang="en">
<head>
<meta charset="utf-8">
<title>PuraGlow – Biotin &amp; Marula Face &amp; Body Oil Labels</title>
<link rel="stylesheet" href="https://fonts.googleapis.com/css2?family=Montserrat:wght@300;400;600&display=swap">
<style>
  :root {
    --canvas: #e1e2e6;
    --green-1: #a4d233;
    --green-2: #84bd2c;
    --olive: #5d7220;
    --olive-logo: #6b7a2a;
    --gold-1: #ebb92d;
    --gold-2: #dca322;
    --gold-soft: #f2c94a;
    --gold-text: #b98a1c;
    --cream: #f8f5ea;
    --blue-1: #62c4ea;
    --blue-2: #48b2e2;
    --blue-text: #1f7fd9;
    --blue-tag: #2d86df;
    --white: #ffffff;
    --paper: #f4f4f2;
  }
  * { box-sizing: border-box; margin: 0; padding: 0; }
  html, body {
    width: 1200px; height: 1200px; overflow: hidden;
    background: var(--canvas);
    font-family: "Montserrat", sans-serif;
  }
  .label-sheet {
    display: grid;
    grid-template-columns: repeat(3, 340px);
    grid-template-rows: repeat(2, 440px);
    gap: 108px 45px;
    padding: 106px 45px;
  }
  .label {
    position: relative; overflow: hidden;
    width: 340px; height: 440px;
    border-radius: 6px;
    background: var(--bg);
    color: var(--ink);
  }
  .label__decor { position: absolute; inset: 0; background: var(--decor); }
  .label__brand {
    position: absolute; top: 30px; left: 0; right: 0;
    text-align: center;
    font-weight: 400; font-size: 30px; letter-spacing: 2px;
    color: var(--logo);
  }
  .label__title {
    position: absolute; top: 146px; left: 60px;
    font-weight: 600; line-height: 0.84;
    font-size: 64px; color: var(--ink);
  }
  .label__title .amp { font-size: 20px; font-weight: 400; margin-left: 4px; }
  .label__subtitle {
    position: absolute; top: 258px; left: 60px;
    font-weight: 300; font-size: 27px; color: var(--sub);
  }
  .label__claim {
    position: absolute; top: 304px; left: 62px;
    padding: 3px 5px;
    font-weight: 400; font-size: 17px;
    background: var(--tag-bg); color: var(--tag-ink);
  }
  .label__volume {
    position: absolute; bottom: 12px; right: 54px;
    font-weight: 400; font-size: 13px; color: var(--vol);
  }

  .label--lime {
    --bg: linear-gradient(160deg, var(--green-1), var(--green-2));
    --decor: radial-gradient(ellipse 70% 55% at 60% 62%, rgba(255,255,255,.18), transparent 70%);
    --ink: var(--white); --sub: #eef8d8; --logo: var(--white);
    --tag-bg: rgba(70,78,50,.72); --tag-ink: #f0f0e8; --vol: #4f6a17;
  }
  .label--leaf {
    --bg: var(--paper);
    --decor: linear-gradient(155deg, transparent 38%, rgba(168,212,70,.55) 52%, var(--green-2) 85%);
    --ink: var(--olive); --sub: #7f8f4a; --logo: var(--olive-logo);
    --tag-bg: rgba(80,90,50,.78); --tag-ink: #f2f2ea; --vol: #55691c;
  }
  .label--amber {
    --bg: linear-gradient(160deg, var(--gold-1), var(--gold-2));
    --decor: radial-gradient(circle 135px at 48% 56%, rgba(240,185,60,.9), rgba(240,185,60,.3) 90%, transparent 100%);
    --ink: var(--white); --sub: #fdebbb; --logo: var(--white);
    --tag-bg: rgba(150,110,40,.72); --tag-ink: #fbf3de; --vol: #a87a16;
  }
  .label--sun {
    --bg: var(--cream);
    --decor: radial-gradient(circle 150px at 43% 55%, var(--gold-soft), #f0c237 75%, rgba(242,215,140,.45) 80%, transparent 100%);
    --ink: var(--gold-text); --sub: #c49a3a; --logo: #a27c2b;
    --tag-bg: rgba(160,120,50,.8); --tag-ink: #fbf3de; --vol: #8f6a16;
  }
  .label--dew {
    --bg: var(--white);
    --decor: radial-gradient(ellipse 48% 45% at 46% 70%, rgba(120,200,235,.75), rgba(150,210,240,.35) 80%, transparent 100%);
    --ink: var(--blue-text); --sub: #4aa3e6; --logo: var(--blue-text);
    --tag-bg: var(--blue-tag); --tag-ink: var(--white); --vol: var(--blue-text);
  }
  .label--sky {
    --bg: linear-gradient(160deg, var(--blue-1), var(--blue-2));
    --decor: radial-gradient(ellipse 45% 45% at 50% 70%, rgba(70,210,240,.8), rgba(90,200,240,.3) 85%, transparent 100%);
    --ink: var(--white); --sub: #e6f6fd; --logo: var(--white);
    --tag-bg: var(--blue-tag); --tag-ink: var(--white); --vol: #2a86d8;
  }
</style>
</head>
<body>
  <main class="label-sheet">
    <section class="label label--lime">
      <div class="label__decor" role="img" aria-label="Soft green leaf illustration"></div>
      <div class="label__brand">PuraGlow</div>
      <h1 class="label__title">Biotin<span class="amp">&amp;</span><br>Marula</h1>
      <p class="label__subtitle">Face &amp; Body Oil</p>
      <p class="label__claim">Moisturizing &amp; Healing</p>
      <p class="label__volume">4oz / 118mL</p>
    </section>
    <section class="label label--leaf">
      <div class="label__decor" role="img" aria-label="Green leaf illustration rising from the lower edge"></div>
      <div class="label__brand">PuraGlow</div>
      <h1 class="label__title">Biotin<span class="amp">&amp;</span><br>Marula</h1>
      <p class="label__subtitle">Face &amp; Body Oil</p>
      <p class="label__claim">Moisturizing &amp; Healing</p>
      <p class="label__volume">4oz / 118mL</p>
    </section>
    <section class="label label--amber">
      <div class="label__decor" role="img" aria-label="Layered golden circles"></div>
      <div class="label__brand">PuraGlow</div>
      <h1 class="label__title">Biotin<span class="amp">&amp;</span><br>Marula</h1>
      <p class="label__subtitle">Face &amp; Body Oil</p>
      <p class="label__claim">Moisturizing &amp; Healing</p>
      <p class="label__volume">4oz / 118mL</p>
    </section>
    <section class="label label--sun">
      <div class="label__decor" role="img" aria-label="Large golden sun circle"></div>
      <div class="label__brand">PuraGlow</div>
      <h1 class="label__title">Biotin<span class="amp">&amp;</span><br>Marula</h1>
      <p class="label__subtitle">Face &amp; Body Oil</p>
      <p class="label__claim">Moisturizing &amp; Healing</p>
      <p class="label__volume">4oz / 118mL</p>
    </section>
    <section class="label label--dew">
      <div class="label__decor" role="img" aria-label="Overlapping light blue water drops"></div>
      <div class="label__brand">PuraGlow</div>
      <h1 class="label__title">Biotin<span class="amp">&amp;</span><br>Marula</h1>
      <p class="label__subtitle">Face &amp; Body Oil</p>
      <p class="label__claim">Moisturizing &amp; Healing</p>
      <p class="label__volume">4oz / 118mL</p>
    </section>
    <section class="label label--sky">
      <div class="label__decor" role="img" aria-label="Overlapping aqua water drops"></div>
      <div class="label__brand">PuraGlow</div>
      <h1 class="label__title">Biotin<span class="amp">&amp;</span><br>Marula</h1>
      <p class="label__subtitle">Face &amp; Body Oil</p>
      <p class="label__claim">Moisturizing &amp; Healing</p>
      <p class="label__volume">4oz / 118mL</p>
    </section>
  </main>
</body>
</html>
```